Logo redesign & Stationery Design Project

We need a logo redesign for our company.

We also require the following stationary with the new logo:
*letterhead
*With compliments slips
*business card
*envelopes

We would like to maintain our current colours of navy blue and gold. We would like to maintain the wording on the back of our current business card.

Our existing letterhead and business card is attached.

Target Market(s)

Medical Professionals, Pharmacists, Lawyers

Industry/Entity Type

Business

Requirements
Must have
• See attached business card and letterhead, as all details on these documents need to be included.

```html
<!DOCTYPE html>
<html lang="en">
<head>
<meta charset="utf-8">
<title>Halden Marsh Stationery</title>
<link href="https://fonts.googleapis.com/css2?family=Questrial&family=PT+Sans&display=swap" rel="stylesheet">
<style>
:root{
  --board:#000;
  --paper:#fff;
  --band:#d3d3d3;
  --navy:#1c1b7c;
  --gold:#c48a12;
  --ink:#2a2a6a;
  --soft:#8795a6;
  --caption:#fff;
}
*{margin:0;padding:0;box-sizing:border-box}
html,body{width:1200px;height:900px;overflow:hidden;background:var(--board)}
body{position:relative;font-family:"Questrial",sans-serif;color:var(--ink)}
.sheet{position:absolute;background:var(--paper);overflow:hidden}
.band{position:absolute;background:var(--band);text-align:center;color:var(--navy)}
.brand-mark{display:block;margin:0 auto;border-radius:50%;background:var(--navy)}
.brand-name{display:block;color:var(--navy);letter-spacing:.5px;white-space:nowrap}
.brand-sub{display:block;color:var(--navy)}
.small{position:absolute;left:0;right:0;font-size:5px;line-height:7px;color:var(--navy)}

/* letterhead */
.letterhead{left:12px;top:22px;width:594px;height:844px}
.letterhead .band.logo{left:53px;top:0;width:132px;height:153px;padding-top:22px}
.letterhead .brand-mark{width:68px;height:68px}
.letterhead .brand-name{font-size:12.5px;margin-top:22px}
.letterhead .brand-sub{font-size:8px;line-height:10px}
.letterhead .footer{left:0;bottom:0;width:594px;height:68px;font-size:8px;line-height:11px;padding-top:9px;color:var(--navy)}
.letterhead .footer p+p+p{margin-top:13px}

/* with compliments slip & envelope */
.slip{left:611px;top:22px;width:579px;height:279px}
.slip .greeting{position:absolute;left:35px;top:37px;font-size:11px;color:#333}
.slip .band.strip{left:415px;top:0;width:130px;height:279px;padding-top:30px}
.envelope{left:611px;top:486px;width:579px;height:259px}
.envelope .band.strip{left:425px;top:0;width:123px;height:259px;padding-top:25px}
.strip .brand-mark{width:62px;height:62px}
.strip .brand-name{font-size:12px;margin-top:22px}
.strip .brand-sub{font-size:8px;line-height:10px}

/* business card */
.card-back{left:611px;top:304px;width:286px;height:178px;overflow:visible}
.card-back .contact{position:absolute;right:92px;top:45px;text-align:right;font-size:9.5px;line-height:11.5px;color:var(--soft)}
.card-back .person{color:#2d5a8c}
.card-back .role{color:#c9b58a;margin-bottom:12px}
.values{position:absolute;left:207px;top:50px;width:94px;height:80px;background:var(--band);padding:6px 4px 0 6px;color:var(--soft);z-index:2;overflow:hidden}
.values .word{display:block;font-size:13px;line-height:13px;letter-spacing:1px;white-space:nowrap}
.values .note{display:block;font-size:5px;line-height:7px;margin-bottom:1px;white-space:nowrap}
.card-front{left:905px;top:305px;width:285px;height:177px;text-align:center}
.card-front .brand-mark{width:82px;height:82px;margin-top:22px}
.card-front .brand-name{font-size:14px;margin-top:29px;color:var(--navy)}
.card-front .brand-sub{font-size:10px;color:var(--soft)}

/* presentation caption */
.specs{position:absolute;left:715px;top:782px;width:400px;text-align:center;font-family:"PT Sans",sans-serif;font-size:16px;line-height:21.5px;color:var(--caption)}
</style>
</head>
<body>

<section class="sheet letterhead">
  <div class="band logo">
    <span class="brand-mark"></span>
    <span class="brand-name">HALDEN MARSH</span>
    <span class="brand-sub">Financial Services</span>
    <span class="brand-sub">ABN 51 600 218 734</span>
  </div>
  <div class="band footer">
    <p>Suite 4, 112-118 Banksia Road, Ridgeview NSW 2231, PO BOX 3408 Millers Bay NSW 2231 | T. 02 9000 4120 | F. 02 9000 4123</p>
    <p>E. office@haldenmarsh.com.au | www.haldenmarsh.com.au</p>
    <p>Corporate Authorised Representative of BKR Wealth Partners AFSL 400218</p>
  </div>
</section>

<section class="sheet slip">
  <p class="greeting">with compliments</p>
  <div class="band strip">
    <span class="brand-mark"></span>
    <span class="brand-name">HALDEN MARSH</span>
    <span class="brand-sub">Financial Services</span>
    <span class="brand-sub">ABN 51 600 218 734</span>
    <div class="small" style="top:208px">Suite 4, 112-118 Banksia Road, Ridgeview NSW<br>2231, PO BOX 3408 Millers Bay NSW 2231<br>T. 02 9000 4120 | F. 02 9000 4123<br>E. office@haldenmarsh.com.au<br>www.haldenmarsh.com.au</div>
    <div class="small" style="top:250px">Corporate Authorised Representative of BKR<br>Wealth Partners AFSL 400218</div>
  </div>
</section>

<section class="sheet card-back">
  <div class="contact">
    <p class="person">Daniel (Dan) Halden</p>
    <p class="role">Partner</p>
    <p>T. 02 9000 4120</p>
    <p>M. 0400 000 381</p>
    <p>E. dan@haldenmarsh.com.au</p>
    <p>Suite 4, 112 Banksia Road, Ridgeview</p>
  </div>
  <div class="values">
    <span class="word">SECURITY</span><span class="note">protective cover planning</span>
    <span class="word">FOCUS</span><span class="note">tailored wealth guidance</span>
    <span class="word">FORESIGHT</span><span class="note">lasting retirement income</span>
  </div>
</section>

<section class="sheet card-front">
  <span class="brand-mark"></span>
  <span class="brand-name">HALDEN MARSH</span>
  <span class="brand-sub">Financial Services</span>
</section>

<section class="sheet envelope">
  <div class="band strip">
    <span class="brand-mark"></span>
    <span class="brand-name">HALDEN MARSH</span>
    <span class="brand-sub">Financial Services</span>
    <span class="brand-sub">ABN 51 600 218 734</span>
    <div class="small" style="top:195px">Suite 4, 112-118 Banksia Road, Ridgeview NSW<br>2231, PO BOX 3408 Millers Bay NSW 2231</div>
    <div class="small" style="top:214px">T. 02 9000 4120 | F. 02 9000 4123<br>E. office@haldenmarsh.com.au<br>www.haldenmarsh.com.au</div>
    <div class="small" style="top:239px">Corporate Authorised Representative of BKR<br>Wealth Partners AFSL 400218</div>
  </div>
</section>

<div class="specs">
  <p>letterhead, paper size : A4</p>
  <p>with compliments : 210 mm x 99 mm</p>
  <p>businesscard : 3.6 in x 2.1 in</p>
  <p>envelope : 9.5 in x 4.125 in</p>
</div>

</body>
</html>
```